Women Web Portal

We are developing an internet portal with content created by and for women in Latin America.
This portal will contain different categories focused on relevant topics for women who are at the same time mothers, lovers, workers, pet-owners, ...

We are looking for design that are at the same time uncluttered, easy-to-use and obvious, and comfy. Pastel colours, buttons using traditional fonts, large space for pictures, highlighted social elements,...

Our target being the middle-class women, we want a design that feels comfortable, real, a bit trendy and traditional, not a Tarsk & Welmore design, something women can relate to and feel comfortable enough to come back and participate.

Examples of websites:
www.dishtable.example
mujer.qelvo.example
www.cabellorinva.example
www.fourneau.example
Updates

Hi dear designers. After viewing some first drafts, I have updated the brief so you might have a better understanding of what we are looking for.

Thanks

Reason: We've been away for a while, unavailable to provide adequate feedback to the designs already sent. So we're extending the deadline in order to give time to everyone to adapt their work according to the feedback we'll be providing today.

Target Market(s)

Women between 25 and 50 years from Latin America. Mainly mothers: basically, we want women to interact with each other and with the content of the site so they create a strong community.

Advertisingly speaking, we want to have users, contents and FMCG brands to live together on this website.

Industry/Entity Type

Internet

Requirements
Must have
• Pastel colours for category tabs. Comfortable look & feel.

The design should include 3 different pages:
- Homepage
- Article page
- User profile

The page will be done in responsive design, so design should be thought to be adapted according to the browser (2 or 3 columns).

Thanks for doing it as a PSD file .

The design should also include:
- 8 category tabs
- Space for 728x90px and 300x600px advertising format.
- A relevant menu bar at the beginning of each page
Nice to have
• News feed/best content/most active comments zone: we need to bring forward content to our users so they'll be attracted to visit more pages of the website.

Small format to register (account).

Slider or any other moving objects.

Any idea that would facilitate and increase user participation
Should not have
• Actual text. please use Lorem Ipsum.

```html
<!DOCTYPE html>
<html lang="en">
<head>
<meta charset="utf-8">
<title>Women Web Portal — Home</title>
<link rel="stylesheet" href="https://fonts.googleapis.com/css2?family=Arimo:wght@400;700&display=swap">
<style>
:root{
  --pink:#d9327c;
  --ink:#222;
  --muted:#8a8a8a;
  --line:#e3e3e3;
  --bar:#e6e6e6;
  --panel:#f6f6f6;
  --black:#050505;
  --white:#fff;
}
*{box-sizing:border-box;margin:0;padding:0}
html,body{width:1200px;height:2931px;overflow:hidden;background:var(--white);font-family:Arimo,Arial,sans-serif;color:var(--ink)}
.page{position:relative;width:1200px;height:2931px}
.abs{position:absolute}
.photo{position:absolute}

/* top bar */
.topbar{left:0;top:0;width:1200px;height:46px;background:var(--pink);color:var(--white);font-size:13px;font-weight:700}
.topbar .network{left:25px;top:15px}
.topbar .net-dot{top:9px;width:26px;height:26px;border-radius:5px;background:rgba(255,255,255,.85)}
.topbar .account{left:757px;top:15px;font-weight:400;font-size:14px}
.topbar .account span{margin:0 26px}
.search{left:928px;top:10px;width:236px;height:26px;background:var(--white);border-radius:3px;color:var(--muted);font-size:12px;font-weight:400;padding:6px 8px}

/* header */
.logo{left:23px;top:104px;font-size:34px;font-weight:700;color:var(--pink);letter-spacing:-.5px}
.slogan{left:61px;top:147px;font-size:13px;color:var(--muted)}
.nav a{position:absolute;top:116px;font-size:13px;color:var(--muted);text-decoration:none}
.nav a.active{top:109px;left:391px;width:74px;height:28px;line-height:28px;text-align:center;background:var(--pink);color:var(--white);border-radius:3px}

.ad{background:var(--black);color:#bbb;display:flex;align-items:center;justify-content:center;text-align:center}
.ad-leader{left:173px;top:216px;width:854px;height:92px;border-radius:3px;font-size:24px}
.ad-sky{left:813px;top:1083px;width:364px;height:618px;font-size:36px;line-height:1.25}

/* slider */
.slider{left:23px;top:374px;width:1154px;height:381px;border:1px solid var(--line)}
.slide-next{left:733px;top:529px;width:56px;height:56px;border-radius:50%;background:#9a9a9a;opacity:.85}
.slide-list .thumb{position:absolute;left:826px;width:107px;height:76px}
.slide-list h3{position:absolute;left:956px;font-size:14px;font-weight:400}
.slide-list p{position:absolute;left:956px;width:210px;font-size:12px;line-height:1.45}

/* category box */
.catbox{left:23px;top:790px;width:752px;height:768px;border:1px solid var(--line)}
.tab{position:absolute;top:801px;font-size:14px;color:var(--pink)}
.tab.active{left:23px;top:790px;width:102px;height:42px;line-height:42px;text-align:center;background:var(--pink);color:var(--white);border-radius:4px}
.tile p{position:absolute;width:352px;font-size:12.5px;line-height:1.6;color:var(--ink)}
.sep{background:var(--bar)}
.more-btn{left:375px;top:1536px;width:42px;height:42px;border-radius:50%;border:1px solid #bbb;background:var(--white)}

/* headings */
.section-title{position:absolute;font-size:23px;color:var(--pink);text-transform:uppercase;font-weight:400}
.intro-title{left:813px;top:784px;color:var(--ink);font-size:25px}
.video{background:var(--black)}
.play{position:absolute;width:40px;height:40px}

/* news */
.news .thumb{position:absolute;left:36px;width:81px;height:76px}
.news h4{position:absolute;left:140px;font-size:18px;font-weight:400}
.news .date{position:absolute;left:140px;font-size:12px;color:var(--muted)}
.news p{position:absolute;left:140px;width:622px;font-size:12px;line-height:1.6}
.news .read{position:absolute;left:689px;font-size:12px;color:var(--pink);text-decoration:underline;background:var(--white);padding-left:4px}

/* share */
.share{left:813px;top:1729px;width:364px;height:350px;background:var(--panel);border:1px solid var(--line)}
.btn-share{position:absolute;width:145px;height:40px;border-radius:5px;color:var(--white);font-size:18px;display:flex;align-items:center;justify-content:flex-end;padding-right:18px}
.btn-share i{width:24px;height:24px;border-radius:4px;background:rgba(255,255,255,.35);margin-right:auto;margin-left:12px}
.like-us{left:932px;top:1962px;font-size:18px;font-weight:700;color:#2c5aa0}
.like-sq{left:1010px;top:1958px;width:32px;height:30px;border:2px solid #2c5aa0;border-radius:4px;background:#e9eefa}
.follow{left:920px;top:2013px;width:150px;height:41px;border-radius:5px;background:#4db4e6;color:var(--white);font-size:15px;text-align:center;line-height:41px}

/* comment form */
.field{position:absolute;background:#efefef;font-size:13px;padding:8px 12px}
.post-btn{left:338px;top:2356px;width:122px;height:39px;line-height:39px;text-align:center;background:#eee;color:#aaa;font-size:13px}

/* testimonials */
.say .thumb{position:absolute;left:816px;width:102px;height:66px}
.say .name{position:absolute;left:928px;font-size:13px}
.say .date{position:absolute;left:928px;font-size:11px;color:var(--muted)}
.say p{position:absolute;left:928px;width:240px;font-size:12px;line-height:1.35}
.say .act{position:absolute;font-size:11px;color:var(--muted)}
.say .act.c{left:1103px;text-decoration:underline}

/* videos */
.vid-cap{position:absolute;font-size:13px;font-weight:700}
.vid-cap span{color:var(--pink);font-weight:400;margin-left:14px}

/* footer */
.footer{left:0;top:2791px;width:1200px;height:140px;background:var(--black);color:var(--white)}
.footer nav{position:absolute;top:44px;width:100%;text-align:center;font-size:12px}
.footer nav span{margin:0 15px}
.footer small{position:absolute;top:94px;width:100%;text-align:center;font-size:13px}
</style>
</head>
<body>
<div class="page">

<svg width="0" height="0" style="position:absolute">
  <defs>
    <g id="play"><circle cx="20" cy="20" r="18" fill="none" stroke="#fff" stroke-width="2"/><path d="M16 12 L28 20 L16 28Z" fill="#fff"/></g>
  </defs>
</svg>

<header>
  <div class="abs topbar">
    <span class="abs network">NETWORK WITH US</span>
    <i class="abs net-dot" style="left:166px"></i>
    <i class="abs net-dot" style="left:198px"></i>
    <i class="abs net-dot" style="left:230px"></i>
    <i class="abs net-dot" style="left:262px"></i>
    <span class="abs account">Register<span>|</span>Sign in</span>
    <div class="abs search">Search any keyword here</div>
  </div>
  <div class="abs logo">LOGO GOES HERE</div>
  <div class="abs slogan">SLOGAN GOES HERE</div>
  <nav class="nav">
    <a class="active">HOME</a>
    <a style="left:486px">ABOUT US</a>
    <a style="left:585px">SERVICES</a>
    <a style="left:686px">WOMEN HEATH</a>
    <a style="left:821px">PET CARE</a>
    <a style="left:923px">CONTACT US</a>
  </nav>
</header>

<div class="abs ad ad-leader">728 X 90&nbsp; ADVERTISEMANT AREA</div>

<section>
  <div class="abs slider"></div>
  <div class="photo" role="img" aria-label="Featured slide photo: mother with smiling baby" style="left:36px;top:386px;width:765px;height:356px;background:linear-gradient(120deg,#c9937a,#f2d7c7 45%,#fbf4ef)"></div>
  <div class="abs slide-next"><svg width="56" height="56"><path d="M24 18 L34 28 L24 38" fill="none" stroke="#fff" stroke-width="4"/></svg></div>
  <div class="slide-list">
    <div class="thumb" role="img" aria-label="Slide thumbnail: family photo" style="top:394px;background:linear-gradient(135deg,#a0654a,#e0b79c)"></div>
    <h3 style="top:394px">HEADIGN GOES HERE</h3>
    <p style="top:425px">"But I must explain to you how all this mistaken idea of denouncing</p>
    <div class="thumb" role="img" aria-label="Slide thumbnail: mother and baby" style="top:521px;background:linear-gradient(135deg,#c9937a,#f2dccf)"></div>
    <h3 style="top:516px">HEADIGN GOES HERE</h3>
    <p style="top:556px">"But I must explain to you how all this mistaken idea of denouncing</p>
    <div class="thumb" role="img" aria-label="Slide thumbnail: smiling woman" style="top:656px;background:linear-gradient(135deg,#b97a55,#f0d3b6)"></div>
    <h3 style="top:652px">HEADIGN GOES HERE</h3>
    <p style="top:690px">"But I must explain to you how all this mistaken idea of denouncing</p>
  </div>
</section>

<section>
  <div class="abs catbox"></div>
  <span class="tab active">Love</span>
  <span class="tab" style="left:137px">Category2</span>
  <span class="tab" style="left:224px">Category3</span>
  <span class="tab" style="left:318px">Category4</span>
  <span class="tab" style="left:407px">Category5</span>
  <span class="tab" style="left:501px">Category6</span>
  <span class="tab" style="left:592px">Category7</span>
  <span class="tab" style="left:684px">Category8</span>

  <div class="tile">
    <div class="photo" role="img" aria-label="Couple lying together smiling" style="left:36px;top:867px;width:350px;height:216px;background:linear-gradient(160deg,#e7eef3,#c88a6a 60%,#a44)"></div>
    <p style="left:36px;top:1100px">"But I must explain to you how all this mistaken idea of denouncing pleasure and praising pain was born and I will</p>
    <div class="photo" role="img" aria-label="Woman reading a book by a river" style="left:414px;top:867px;width:351px;height:216px;background:linear-gradient(160deg,#3d4a2c,#6c7a55 50%,#262b1c)"></div>
    <p style="left:414px;top:1100px">"But I must explain to you how all this mistaken idea of denouncing pleasure and praising pain was born and I will</p>
  </div>
  <div class="abs sep" style="left:36px;top:1172px;width:729px;height:15px"></div>
  <div class="tile">
    <div class="photo" role="img" aria-label="Couple under an umbrella in the rain at night" style="left:36px;top:1218px;width:350px;height:218px;background:radial-gradient(circle at 55% 40%,#8a7250,#2b2418 60%,#0f0c08)"></div>
    <p style="left:36px;top:1451px">"But I must explain to you how all this mistaken idea of denouncing pleasure and praising pain was born and I will</p>
    <div class="photo" role="img" aria-label="Couple with a red rose" style="left:414px;top:1218px;width:351px;height:218px;background:linear-gradient(120deg,#3a2a22,#b57a55 50%,#c7a040)"></div>
    <p style="left:414px;top:1451px">"But I must explain to you how all this mistaken idea of denouncing pleasure and praising pain was born and I will</p>
  </div>
  <div class="abs more-btn"><svg width="40" height="40"><path d="M13 16 L20 23 L27 16" fill="none" stroke="#999" stroke-width="2"/></svg></div>
</section>

<aside>
  <h2 class="section-title intro-title">INTRODUCTION</h2>
  <div class="abs video" style="left:813px;top:841px;width:364px;height:211px"><svg class="play" style="left:162px;top:86px"><use href="#play"/></svg></div>
  <div class="abs ad ad-sky">300 x 600<br>Advertisement Area</div>

  <div class="abs share"></div>
  <div class="btn-share" style="left:834px;top:1762px;background:#3b5998"><i></i>SHARE</div>
  <div class="btn-share" style="left:1014px;top:1762px;background:#e9e9e9;color:#222;border:1px solid #ccc"><i style="background:#ccc"></i>SHARE</div>
  <div class="btn-share" style="left:834px;top:1818px;background:#d9342b"><i></i>SHARE</div>
  <div class="btn-share" style="left:1014px;top:1818px;background:#7fcfe9"><i></i>SHARE</div>
  <div class="btn-share" style="left:834px;top:1874px;background:#f07b1c"><i></i>SHARE</div>
  <div class="btn-share" style="left:1014px;top:1874px;background:#f48a2a"><i></i>SHARE</div>
  <span class="abs like-us">LIKE US</span>
  <i class="abs like-sq"></i>
  <div class="abs follow">Follow us</div>
</aside>

<section class="news">
  <h2 class="section-title" style="left:30px;top:1628px">LATEST NEWS</h2>

  <div class="thumb" role="img" aria-label="Author portrait" style="top:1685px;background:linear-gradient(135deg,#7a5a3a,#e4c29a)"></div>
  <h4 style="top:1683px">Head line Goes Here</h4>
  <span class="date" style="top:1710px">My 3-2013 , Sunday 9:11 pm</span>
  <p style="top:1728px">"But I must explain to you how all this mistaken idea of denouncing pleasure and praising pain was born and I will give you a complete account of the system, and expound the actual teachings of the g</p>
  <a class="read" style="top:1747px">READ MORE</a>
  <div class="abs" style="left:36px;top:1795px;width:729px;height:1px;background:var(--line)"></div>

  <div class="thumb" role="img" aria-label="Author portrait" style="top:1820px;background:linear-gradient(135deg,#7a5a3a,#e4c29a)"></div>
  <h4 style="top:1818px">Head line Goes Here</h4>
  <span class="date" style="top:1845px">My 3-2013 , Sunday 9:11 pm</span>
  <p style="top:1863px">"But I must explain to you how all this mistaken idea of denouncing pleasure and praising pain was born and I will give you a complete account of the system, and expound the actual teachings of the g</p>
  <a class="read" style="top:1882px">READ MORE</a>
  <div class="abs" style="left:36px;top:1924px;width:729px;height:1px;background:var(--line)"></div>

  <div class="thumb" role="img" aria-label="Author portrait" style="top:1947px;background:linear-gradient(135deg,#7a5a3a,#e4c29a)"></div>
  <h4 style="top:1943px">Head line Goes Here</h4>
  <span class="date" style="top:1970px">My 3-2013 , Sunday 9:11 pm</span>
  <p style="top:1988px">"But I must explain to you how all this mistaken idea of denouncing pleasure and praising pain was born and I will give you a complete account of the system, and expound the actual teachings of the g</p>
  <a class="read" style="top:2007px">READ MORE</a>
</section>

<div class="abs sep" style="left:23px;top:2122px;width:752px;height:13px"></div>
<div class="abs sep" style="left:813px;top:2122px;width:364px;height:13px"></div>

<section>
  <h2 class="section-title" style="left:23px;top:2168px">POST&nbsp; YOUR COMMENT</h2>
  <div class="field" style="left:36px;top:2219px;width:343px;height:30px">Name</div>
  <div class="field" style="left:36px;top:2262px;width:343px;height:30px">Email address</div>
  <div class="field" style="left:36px;top:2303px;width:343px;height:30px">Subject</div>
  <div class="field" style="left:422px;top:2217px;width:341px;height:117px">Your Comment ...</div>
  <div class="abs post-btn">POST NOW</div>
</section>

<section class="say">
  <h2 class="section-title" style="left:813px;top:2168px;font-size:21px">WHAT PEOPLE SAY ABOUT US</h2>

  <div class="thumb" role="img" aria-label="Client portrait" style="top:2219px;background:linear-gradient(135deg,#6d6355,#d8c8b0)"></div>
  <span class="name" style="top:2216px">Client Name</span>
  <span class="date" style="top:2234px">My 3-2013 , Sunday 9:11 pm</span>
  <p style="top:2250px">"But I must explain to you how all this mistaken idea of denouncing pleasure and praising pain was born and I will give you</p>
  <span class="act" style="left:963px;top:2306px">Like</span><span class="act c" style="top:2306px">Comment</span>

  <div class="thumb" role="img" aria-label="Client portrait" style="top:2341px;background:linear-gradient(135deg,#6d6355,#d8c8b0)"></div>
  <span class="name" style="top:2338px">Client Name</span>
  <span class="date" style="top:2356px">My 3-2013 , Sunday 9:11 pm</span>
  <p style="top:2372px">"But I must explain to you how all this mistaken idea of denouncing pleasure and praising pain was born and I will give you</p>
  <span class="act" style="left:963px;top:2428px">Like</span><span class="act c" style="top:2428px">Comment</span>

  <div class="thumb" role="img" aria-label="Client portrait" style="top:2463px;background:linear-gradient(135deg,#6d6355,#d8c8b0)"></div>
  <span class="name" style="top:2460px">Client Name</span>
  <span class="date" style="top:2478px">My 3-2013 , Sunday 9:11 pm</span>
  <p style="top:2494px">"But I must explain to you how all this mistaken idea of denouncing pleasure and praising pain was born and I will give you</p>
  <span class="act" style="left:963px;top:2550px">Like</span><span class="act c" style="top:2550px">Comment</span>

  <div class="thumb" role="img" aria-label="Client portrait" style="top:2588px;background:linear-gradient(135deg,#6d6355,#d8c8b0)"></div>
  <span class="name" style="top:2585px">Client Name</span>
  <span class="date" style="top:2603px">My 3-2013 , Sunday 9:11 pm</span>
  <p style="top:2619px">"But I must explain to you how all this mistaken idea of denouncing pleasure and praising pain was born and I will give you</p>
  <span class="act" style="left:963px;top:2675px">Like</span><span class="act c" style="top:2675px">Comment</span>
</section>

<section>
  <h2 class="section-title" style="left:23px;top:2478px">LATEST VIDEO</h2>
  <div class="abs video" style="left:23px;top:2539px;width:208px;height:122px"><svg class="play" style="left:84px;top:41px"><use href="#play"/></svg></div>
  <div class="abs video" style="left:295px;top:2539px;width:216px;height:122px"><svg class="play" style="left:88px;top:41px"><use href="#play"/></svg></div>
  <div class="abs video" style="left:557px;top:2539px;width:208px;height:122px"><svg class="play" style="left:84px;top:41px"><use href="#play"/></svg></div>
  <span class="vid-cap" style="left:23px;top:2669px">Video Heading<span>View : 700 Users</span></span>
  <span class="vid-cap" style="left:295px;top:2669px">Video Heading<span>View : 700 Users</span></span>
  <span class="vid-cap" style="left:557px;top:2669px">Video Heading<span>View : 700 Users</span></span>
</section>

<footer class="abs footer">
  <nav><span>HOME</span><span>ABOUT US</span><span>SERVICES</span><span>WOMEN HEATH</span><span>PET CARE</span><span>CONTACT US</span></nav>
  <small>All copyright are reserved by company name</small>
</footer>

</div>
</body>
</html>
```